Quolvex custom business card design

Need a authentic, innovative business card design for a new mobile app business. I am uploading a few screen images from our app for you to view. I would like app design theme to match business card design. I can also send logo images.

```html
<!DOCTYPE html>
<html lang="en">
<head>
<meta charset="utf-8">
<title>Quolvex Business Card</title>
<link rel="stylesheet" href="https://fonts.googleapis.com/css2?family=Montserrat:wght@700;800&family=Open+Sans:wght@400&display=swap">
<style>
  :root {
    --page-bg: #e9e7e4;
    --brand-purple: #62008f;
    --brand-black: #1e1e1e;
    --text-light: #ffffff;
    --disc-light: #ffffff;
    --disc-mid: #ededed;
    --disc-edge: #cfcfcf;
  }
  * { margin: 0; padding: 0; box-sizing: border-box; }
  html, body {
    width: 1200px;
    height: 900px;
    overflow: hidden;
    background: var(--page-bg);
  }
  .business-card {
    position: absolute;
    left: 145px;
    top: 168px;
    width: 910px;
    height: 565px;
    background: var(--brand-purple);
    overflow: hidden;
    box-shadow: 0 10px 30px rgba(0,0,0,0.18);
  }
  .dark-strip {
    position: absolute;
    right: 0;
    top: 0;
    width: 265px;
    height: 100%;
    background: var(--brand-black);
  }
  .brand-disc {
    position: absolute;
    left: 400px;
    top: 37px;
    width: 490px;
    height: 490px;
    border-radius: 50%;
    background: radial-gradient(circle at 40% 35%, var(--disc-light) 0%, var(--disc-mid) 60%, var(--disc-edge) 100%);
    display: flex;
    align-items: center;
    justify-content: center;
  }
  .brand-name {
    font-family: "Montserrat", sans-serif;
    font-weight: 800;
    font-size: 68px;
    color: var(--brand-black);
    letter-spacing: 0.5px;
  }
  .holder {
    position: absolute;
    left: 56px;
    top: 66px;
    color: var(--text-light);
  }
  .holder-name {
    font-family: "Montserrat", sans-serif;
    font-weight: 700;
    font-size: 34px;
    line-height: 40px;
    letter-spacing: 0.3px;
  }
  .holder-title {
    font-family: "Open Sans", sans-serif;
    font-size: 25px;
    line-height: 30px;
  }
  .contact-list {
    position: absolute;
    left: 56px;
    top: 280px;
    list-style: none;
    color: var(--text-light);
    font-family: "Open Sans", sans-serif;
    font-size: 26px;
    line-height: 33.5px;
  }
  .contact-list li {
    display: flex;
    align-items: center;
    gap: 6px;
  }
  .contact-icon {
    width: 20px;
    height: 20px;
    fill: var(--text-light);
    flex: none;
  }
  .postal-address {
    position: absolute;
    left: 56px;
    top: 437px;
    color: var(--text-light);
    font-family: "Open Sans", sans-serif;
    font-style: normal;
    font-size: 26px;
    line-height: 33px;
  }
</style>
</head>
<body>
  <div class="business-card">
    <div class="dark-strip"></div>

    <div class="holder">
      <p class="holder-name">DANIEL MORROW</p>
      <p class="holder-title">Managing Director</p>
    </div>

    <ul class="contact-list">
      <li>
        <svg class="contact-icon" viewBox="0 0 20 20" aria-hidden="true">
          <path d="M2 7c0-3 4-4 8-4s8 1 8 4v2h-4V7.5c-1-.6-2.4-.9-4-.9s-3 .3-4 .9V9H2z"/>
          <path d="M5 10l2-2h6l2 2 2 7H3z"/>
        </svg>
        <span>044-555 019 283</span>
      </li>
      <li>
        <svg class="contact-icon" viewBox="0 0 20 20" aria-hidden="true">
          <path d="M6 1h8a1.5 1.5 0 0 1 1.5 1.5v15A1.5 1.5 0 0 1 14 19H6a1.5 1.5 0 0 1-1.5-1.5v-15A1.5 1.5 0 0 1 6 1zm0.5 2.5v11h7v-11zM10 15.6a1.1 1.1 0 1 0 0 2.2 1.1 1.1 0 0 0 0-2.2z"/>
        </svg>
        <span>044-555 019 283</span>
      </li>
      <li>
        <svg class="contact-icon" viewBox="0 0 20 20" aria-hidden="true">
          <path d="M2 4h16v1.2l-8 5.5-8-5.5zM2 7.2l8 5.5 8-5.5V16H2z"/>
        </svg>
        <span>info@quolvexapp.com</span>
      </li>
      <li>
        <svg class="contact-icon" viewBox="0 0 20 20" aria-hidden="true">
          <path d="M10 1.5a8.5 8.5 0 1 0 0 17 8.5 8.5 0 0 0 0-17zm-1 2.2c-.6 1.2-2.6 1.4-2.8 3-.2 1.3 1.6 1.5 2.4 2.6.7 1-.4 2.4.3 3.6.5.9 1.4 1.5 1.3 3.1A6.5 6.5 0 0 1 3.6 9.6c.6-.1 1.4.5 1.8-.3.5-1.2-.3-2.6.5-3.6A6.5 6.5 0 0 1 9 3.7zm4 1.1a6.5 6.5 0 0 1 3.2 6.9c-.8-.4-1.6-1.4-2.6-1.1-1 .3-.7 1.8-1.6 2.1-.9.3-1.8-.9-1.6-2 .2-1.2 1.8-1.2 2.2-2.4.4-1.2-.6-2.1.4-3.5z"/>
        </svg>
        <span>www.quolvexapp.com</span>
      </li>
    </ul>

    <address class="postal-address">
      12345, Address Goes Here<br>
      Country Name, 123456
    </address>

    <div class="brand-disc">
      <span class="brand-name">Quolvex</span>
    </div>
  </div>
</body>
</html>
```